Tumbler Cafe - Menu Redesign

What We Want

We're looking for a bold redesign of our current menu. Our current menu is tired and boring and does not accurately reflect our revitalization of the Tumbler Cafe brand. Attachments will be submitted with the campaign for menu items.

Design Guidelines

• Creative use of typography and color. Think Bold, Fun, Loud and uninhibited.
• Fluid, easy to read, layout that emphasizes readability.
• The subtle, demure, look of typographic columns (examples below in resources)
• Creative use of 'wells' for menu item highlights as well as great boarders
• Loud typefaces as long as readability is the focus & emphasis.
• Small illustrations/icons but they must not effect or take the focus from the readability of the menu
• Big, oversized, menu that will look great on recycled paper
• Subtle watermarks/illustrations
• creative use of textures / highlights / section breaks

Menu Requirements

• 9”x12” paper size. Please notify us if your design works better in a different format.
• Oversized, designed for printing on recycled paper.
• Single Page Menu (use lunch on front and breakfast on back)
• Do not use $ or "..." in pricing. Please space all prices equally.
• Simplistic layout that emphasizes readability and logical navigation of menu items.
• Acceptable file types
• Photoshop
• Indesign
• illustrator
• Please contact us before you submit a design if you plan on using something else
• HTML/CSS would be a huge benefit. It's not a must, but it will definitely help you win the award.
• Must retain some of our current color scheme (red/orange/yellow – see attachments/website).

NOTE: Please download ALL attached resources for the project.
Updates

Current web site:  www.tumblercafe-example.com

please read attachment:  tumbler_menu_redesign_request.docx

Lots of good information & examples on menus we like and the design elements featured in the menu.

All,

Thanks for your design submissions!  With all the designs that have be submitted so far, we are confident that our money will be well spent.  I have changed the project to non-refundable.  Please continue working on your designs using the design_request doc that's posted for guidelines/requirements.  I will provide specific feedback to designs as needed.

For your convenience:

Design Guidelines

 

Creativeuse of typography and color.  Think Bold,Fun, Loud and uninhibited.

Fluid,easy to read, layout that emphasizes readability.

Thesubtle, demure, look of typographic columns (examples below in resources)

Creativeuse of 'wells' for menu item highlights as well as great boarders

Loudtypefaces as long as readability is the focus & emphasis.

Smallillustrations/icons but they must not effect or take the focus from thereadability of the menu

Big,oversized, menu that will look great on recycled paper

Subtlewatermarks/illustrations

creativeuse of textures / highlights / section breaks

 

  MenuRequirements

 

9”x12”paper size.  Please notify us if yourdesign works better in a different format.

Oversized,designed for printing on recycled paper.

SinglePage Menu (use lunch on front and breakfast on back)

Donot use $ or "..." in pricing.Please space all prices equally.

Simplisticlayout that emphasizes readability and logical navigation of menu items.

Acceptablefile types

Photoshop

Indesign

illustrator 

Pleasecontact us before you submit a design if you plan on using something else

HTML/CSSwould be a huge benefit.  It's not amust, but it will definitely help you win the award.

Mustretain some of our current color scheme (red/orange/yellow – seeattachments/website). 

 

Do Not Use

 

Skeuomorphismin any way.

Wedo not want any actual pictures of food on the menu (subtle illustrations /icons are great and encouraged).

Typefacesthat are hard to read.

Thanks!

dana

Reason: need to incorporate changes to menu / menu items

Please expect some new copy tonight (USA EST) for the breakfast menu items.  Thanks!

dana

COPY UPDATE:  Please check new menu item listing (revision 3) for updated copy.  Please revisit all menu items as I have grouped, consolidated, and eliminated some items.

Thanks!

dana 

DESIGN UPDATE:  I added an omelette hero/jumbotron design that we'd like to use to display the omelettes on the breakfast menu.  It doesn't have to be exactly like this one, it's just meant to be a guideline.  Please take a look and see if you can fit it in to your design.  Also, the copy has been updated for the breakfast & lunch menus.

Reason: Revised design changes not yet received.

Reason: Designer needs more tine to complete final submission. This will be the last extension. Thanks! dana

Target Market(s)

Women - 60% or more. Mostly professionals. 18-55.
Men - Professionals mostly. Judges, Attorneys, Agents, Ect. Ages 18-55.

Industry/Entity Type

Printing

Colors
f37022
ec1f27
f78f20
faa54b
f04a50
fee18a
faee3e

Requirements
Must have
• see menu requirements in task description.
Nice to have
• Design Ideas We Love

http://www.menugallery-example.com/menucraft/archives/stonegate_inn.php
We like: typefaces, typographic columns & layout, use of butcher-block print, simplicity
We don't like: lack of bold, color lack of textures, lack of general vitality in the brand, no use of icons/illustrations

http://www.menugallery-example.com/menucraft/archives/patty_vault.php
We like: typefaces, bold headers & section breaks, texturized typefaces, use of illustrations, and specifically we love how they did the 'custom creation' menu
We don't like: lack of bold color, lack of subtle texturing, little more use of illustrated icons would be nice

http://www.menugallery-example.com/menucraft/archives/the_rowdy_roost.php
We like: use of bold colors, organization & layout, the section highlights are nice
We don't like: lack of textures, lack subtle illustrations/icons.

http://www.menugallery-example.com/menucraft/archives/wexford_mill.php
We like: use of textures, typefaces, layout & organization, single page menu
We don't like: lack of textures, lack of bold color, lack of icons and menu item hightlights

http://www.menugallery-example.com/menucraft/archives/zibbo_caf.php
We like: use of texturing, typesfaces, layout & organization, creative use of illustrations/icons, bold colors
We don't like: not a huge fan of the bordering; and illustrations take up too much room for single page menu

http://www.menugallery-example.com/menucraft/archives/ved_hjornet_af_torvet.php
We like: creative use of typefaces, organization & layout, cool illustrations, oversized menu, section seperators are cool & unique
We don't like: lack of textures, menu items inside illustrations, typefaces can get hard to read in certain areas
Should not have
• Do Not Use

• Skeuomorphism in any way.
• We do not want any actual pictures of food on the menu (subtle illustrations / icons are great and encouraged).
• Typefaces that are hard to read.

```html
<!DOCTYPE html>
<html lang="en">
<head>
<meta charset="utf-8">
<title>Tumbler Cafe Lunch Menu</title>
<link href="https://fonts.googleapis.com/css2?family=Oswald:wght@500;700&family=Open+Sans:wght@400;700&display=swap" rel="stylesheet">
<style>
  :root{
    --red:#ec1f27;
    --orange:#f37022;
    --amber:#f78f20;
    --yellow:#fee18a;
    --lemon:#faee3e;
    --ink:#1d1d1d;
    --muted:#555;
    --paper:#ffffff;
  }
  *{box-sizing:border-box;margin:0;padding:0}
  html,body{width:900px;height:1200px;overflow:hidden;background:var(--paper)}
  .menu{position:relative;width:900px;height:1200px;background:var(--paper);font-family:"Open Sans",sans-serif;color:var(--ink)}
  .edge{position:absolute;top:0;bottom:0;width:16px;background:var(--red)}
  .edge--left{left:0;border-right:4px solid var(--lemon)}
  .edge--right{right:0;border-left:4px solid var(--lemon)}
  .band{position:absolute;left:0;right:0;height:8px;background:linear-gradient(90deg,var(--orange),var(--amber),var(--orange))}
  .band--top{top:0}
  .band--bottom{bottom:0}
  .column{position:absolute;top:26px;width:395px}
  .column--left{left:40px}
  .column--right{left:470px}
  .section{margin-bottom:14px}
  .section__title{font-family:"Oswald",sans-serif;font-weight:700;font-size:19px;letter-spacing:.5px;text-transform:uppercase;line-height:1.1;display:flex;align-items:center;gap:10px}
  .section__note{font-size:8.5px;color:var(--muted);line-height:1.3;margin:3px 0 6px}
  .item{margin-bottom:5px;line-height:1.2}
  .item__name{font-family:"Oswald",sans-serif;font-weight:500;font-size:10.5px;text-transform:uppercase;letter-spacing:.3px}
  .item__price{color:var(--red);margin-left:6px}
  .item__desc{font-size:8.5px;color:var(--muted)}
  .icon{display:inline-block;width:14px;height:24px;border-radius:4px 4px 2px 2px;background:linear-gradient(var(--red),var(--orange))}
  .icon--pale{background:linear-gradient(#bbb,#888)}
  .figures{position:absolute;left:40px;bottom:22px;width:200px;height:44px;background:linear-gradient(90deg,var(--orange),var(--red));border-radius:4px;opacity:.85}
  .badges{position:absolute;right:48px;top:905px;display:flex;gap:8px}
  .badge{width:22px;height:22px;border-radius:50%;border:2px solid var(--ink)}
</style>
</head>
<body>
<div class="menu">
  <div class="edge edge--left"></div>
  <div class="edge edge--right"></div>
  <div class="band band--top"></div>
  <div class="band band--bottom"></div>

  <div class="column column--left">
    <section class="section">
      <h2 class="section__title">Cold Sandwiches <span class="icon" role="img" aria-label="Small shaker illustration"></span><span class="icon icon--pale" role="img" aria-label="Small shaker illustration"></span></h2>
      <p class="section__note">Served on your choice of bread with lettuce, tomato and a pickle spear. Add a cup of soup 2.50</p>
      <div class="item"><div class="item__name">BLT<span class="item__price">5.95</span></div><div class="item__desc">Thick cut bacon, crisp lettuce and ripe tomato</div></div>
      <div class="item"><div class="item__name">Tumbler Chicken Salad<span class="item__price">6.75</span></div><div class="item__desc">House chicken salad with celery, grapes and pecans</div></div>
      <div class="item"><div class="item__name">Turkey Club<span class="item__price">7.50</span></div><div class="item__desc">Roast turkey, bacon, Swiss and mayo on toasted bread</div></div>
      <div class="item"><div class="item__name">Egg Salad<span class="item__price">5.50</span></div><div class="item__desc">Fresh egg salad with chives on wheat or white</div></div>
      <div class="item"><div class="item__name">Tuna Salad<span class="item__price">6.25</span></div><div class="item__desc">Albacore tuna with dill and red onion</div></div>
      <div class="item"><div class="item__name">Turkey Sandwich<span class="item__price">6.50</span></div><div class="item__desc">Sliced turkey breast, provolone and honey mustard</div></div>
      <div class="item"><div class="item__name">Chicken Salad Club<span class="item__price">7.25</span></div><div class="item__desc">Chicken salad stacked with bacon and cheddar</div></div>
      <div class="item"><div class="item__name">Ham &amp; Swiss<span class="item__price">6.25</span></div><div class="item__desc">Smoked ham, Swiss cheese and spicy brown mustard</div></div>
      <div class="item"><div class="item__name">Tuna Sub<span class="item__price">6.95</span></div><div class="item__desc">Tuna salad on a toasted roll with provolone</div></div>
    </section>

    <section class="section">
      <h2 class="section__title">Wraps</h2>
      <p class="section__note">Wrapped in a warm flour tortilla and served with your choice of side</p>
      <div class="item"><div class="item__name">Veggie Wrap<span class="item__price">6.50</span></div><div class="item__desc">Spinach, peppers, cucumber, sprouts and hummus</div></div>
      <div class="item"><div class="item__name">Spicy Chicken Wrap<span class="item__price">7.25</span></div><div class="item__desc">Grilled chicken, jalapeños, pepper jack and chipotle sauce</div></div>
      <div class="item"><div class="item__name">Thai Chicken Wrap<span class="item__price">7.25</span></div><div class="item__desc">Chicken, peanut sauce, cabbage and carrots</div></div>
      <div class="item"><div class="item__name">Philly Cheese Steak Wrap<span class="item__price">7.95</span></div><div class="item__desc">Shaved steak, onions, peppers and melted provolone</div></div>
      <div class="item"><div class="item__name">Mediterranean Wrap<span class="item__price">6.95</span></div><div class="item__desc">Feta, olives, tomato, romaine and Greek dressing</div></div>
      <div class="item"><div class="item__name">Turkey Cheddar Wrap<span class="item__price">6.95</span></div><div class="item__desc">Turkey, cheddar, lettuce, tomato and ranch</div></div>
      <div class="item"><div class="item__name">Buffalo Chicken Wrap<span class="item__price">7.25</span></div><div class="item__desc">Crispy chicken tossed in buffalo sauce with blue cheese</div></div>
      <div class="item"><div class="item__name">Tuna Melt Wrap<span class="item__price">6.95</span></div><div class="item__desc">Tuna salad and Swiss pressed until golden</div></div>
    </section>

    <section class="section">
      <h2 class="section__title">Tumbler Burgers</h2>
      <p class="section__note">Half pound burgers cooked to order with lettuce, tomato and onion</p>
      <div class="item"><div class="item__name">Hamburger<span class="item__price">6.95</span></div><div class="item__desc">Our classic burger on a toasted brioche bun</div></div>
      <div class="item"><div class="item__name">Cheeseburger<span class="item__price">7.50</span></div><div class="item__desc">Choice of American, cheddar, Swiss or pepper jack</div></div>
      <div class="item"><div class="item__name">Bacon Cheeseburger<span class="item__price">8.25</span></div><div class="item__desc">Crisp bacon and cheddar stacked high</div></div>
      <div class="item"><div class="item__name">Mushroom Swiss Burger<span class="item__price">8.25</span></div><div class="item__desc">Sautéed mushrooms and melted Swiss cheese</div></div>
      <div class="item"><div class="item__name">Black Bean Burger<span class="item__price">7.25</span></div><div class="item__desc">House made patty with avocado and salsa</div></div>
      <div class="item"><div class="item__name">BBQ Burger<span class="item__price">8.25</span></div><div class="item__desc">Smoky barbecue sauce, onion rings and cheddar</div></div>
      <div class="item"><div class="item__name">Patty Melt<span class="item__price">7.95</span></div><div class="item__desc">Grilled onions and Swiss on toasted rye</div></div>
      <div class="item"><div class="item__name">Turkey Burger<span class="item__price">7.50</span></div><div class="item__desc">Lean turkey patty with cranberry mayo</div></div>
      <div class="item"><div class="item__name">Southwest Burger<span class="item__price">8.25</span></div><div class="item__desc">Pepper jack, jalapeños and chipotle mayo</div></div>
    </section>
  </div>

  <div class="column column--right">
    <section class="section">
      <h2 class="section__title">Signature Sandwiches <span class="icon" role="img" aria-label="Small shaker illustration"></span></h2>
      <p class="section__note">Our most loved sandwiches, served with chips or fries and a pickle spear</p>
      <div class="item"><div class="item__name">Grilled Chicken Club<span class="item__price">8.50</span></div><div class="item__desc">Grilled chicken, bacon, Swiss, lettuce and tomato</div></div>
      <div class="item"><div class="item__name">Grilled Chicken Sandwich<span class="item__price">7.50</span></div><div class="item__desc">Marinated chicken breast with lettuce and tomato</div></div>
      <div class="item"><div class="item__name">Chicken Philly<span class="item__price">7.95</span></div><div class="item__desc">Shaved chicken, peppers, onions and provolone</div></div>
      <div class="item"><div class="item__name">Reuben<span class="item__price">8.25</span></div><div class="item__desc">Corned beef, sauerkraut, Swiss and Russian on rye</div></div>
      <div class="item"><div class="item__name">Tuna Melt<span class="item__price">6.95</span></div><div class="item__desc">Tuna salad with melted American on grilled bread</div></div>
      <div class="item"><div class="item__name">Cuban<span class="item__price">8.25</span></div><div class="item__desc">Roast pork, ham, Swiss, pickles and mustard pressed</div></div>
      <div class="item"><div class="item__name">Grilled Cheese<span class="item__price">4.95</span></div><div class="item__desc">Three cheeses melted on thick Texas toast</div></div>
      <div class="item"><div class="item__name">Buffalo Chicken Sandwich<span class="item__price">7.95</span></div><div class="item__desc">Crispy chicken, buffalo sauce and blue cheese</div></div>
      <div class="item"><div class="item__name">Philly Cheese Steak<span class="item__price">8.50</span></div><div class="item__desc">Shaved steak with onions, peppers and provolone</div></div>
      <div class="item"><div class="item__name">French Dip<span class="item__price">8.25</span></div><div class="item__desc">Roast beef and Swiss with warm au jus</div></div>
      <div class="item"><div class="item__name">Meatball Sub<span class="item__price">7.50</span></div><div class="item__desc">House meatballs, marinara and mozzarella</div></div>
      <div class="item"><div class="item__name">Hot Pastrami<span class="item__price">8.25</span></div><div class="item__desc">Pastrami, Swiss and deli mustard on rye</div></div>
      <div class="item"><div class="item__name">Veggie Melt<span class="item__price">6.95</span></div><div class="item__desc">Grilled vegetables and provolone on sourdough</div></div>
    </section>

    <section class="section">
      <h2 class="section__title">Tumbler Signatures <span class="icon" role="img" aria-label="Small shaker illustration"></span></h2>
      <p class="section__note">House favorites made fresh every day in our kitchen</p>
      <div class="item"><div class="item__name">Chicken Tenders<span class="item__price">7.50</span></div><div class="item__desc">Hand breaded tenders with honey mustard and fries</div></div>
      <div class="item"><div class="item__name">Fish &amp; Chips<span class="item__price">8.95</span></div><div class="item__desc">Beer battered cod with tartar sauce and coleslaw</div></div>
      <div class="item"><div class="item__name">Turkey Platter<span class="item__price">8.50</span></div><div class="item__desc">Sliced turkey, mashed potatoes, gravy and green beans</div></div>
      <div class="item"><div class="item__name">Chicken Pot Pie<span class="item__price">7.95</span></div><div class="item__desc">Creamy chicken and vegetables under a flaky crust</div></div>
      <div class="item"><div class="item__name">Quesadilla<span class="item__price">6.95</span></div><div class="item__desc">Chicken or steak with peppers, onions and cheddar</div></div>
      <div class="item"><div class="item__name">Chicken Parmesan<span class="item__price">8.95</span></div><div class="item__desc">Breaded chicken, marinara and mozzarella over pasta</div></div>
      <div class="item"><div class="item__name">Shrimp Basket<span class="item__price">9.25</span></div><div class="item__desc">Fried shrimp with cocktail sauce and fries</div></div>
      <div class="item"><div class="item__name">Meatloaf<span class="item__price">8.50</span></div><div class="item__desc">Homestyle meatloaf with mashed potatoes</div></div>
      <div class="item"><div class="item__name">Chili Bowl<span class="item__price">5.95</span></div><div class="item__desc">Beef and bean chili topped with cheddar and onion</div></div>
      <div class="item"><div class="item__name">Soup &amp; Salad<span class="item__price">6.95</span></div><div class="item__desc">Cup of soup with a garden side salad</div></div>
      <div class="item"><div class="item__name">Mac &amp; Cheese<span class="item__price">6.50</span></div><div class="item__desc">Baked with three cheeses and crumb topping</div></div>
      <div class="item"><div class="item__name">Gyro Platter<span class="item__price">8.95</span></div><div class="item__desc">Seasoned lamb, tzatziki, pita and Greek salad</div></div>
      <div class="item"><div class="item__name">Veggie Stir Fry<span class="item__price">7.50</span></div><div class="item__desc">Seasonal vegetables in ginger soy over rice</div></div>
    </section>
  </div>

  <div class="badges"><span class="badge"></span><span class="badge"></span></div>
  <div class="figures" role="img" aria-label="Row of small salt and pepper shaker illustrations"></div>
</div>
</body>
</html>
```